Bright Crest Lifts

im looking for someone to help me with my letterhead design. i have already got my logo design just need help with this part

Industry/Entity Type

Construction

Colors
0255a3

Requirements
Must have
• must have all my details eg. bank details, abn and acn

```html
<!DOCTYPE html>
<html lang="en">
<head>
<meta charset="utf-8">
<title>Bright Crest Lifts Letterhead</title>
<link href="https://fonts.googleapis.com/css2?family=Arimo:wght@400;700&display=swap" rel="stylesheet">
<style>
  :root {
    --backdrop: #6a6a6a;
    --paper: #ffffff;
    --brand-blue: #0a7ac4;
    --brand-deep: #0255a3;
    --mark-faint: #e3eef7;
  }
  * { margin: 0; padding: 0; box-sizing: border-box; }
  html, body {
    width: 1200px;
    height: 848px;
    overflow: hidden;
    background: var(--backdrop);
    font-family: "Arimo", Arial, sans-serif;
  }
  .letterhead {
    position: absolute;
    left: 329px;
    top: 17px;
    width: 576px;
    height: 816px;
    background: var(--paper);
    overflow: hidden;
  }
  .brand-name {
    position: absolute;
    left: 0;
    right: 0;
    top: 24px;
    text-align: center;
    font-weight: 700;
    font-size: 26px;
    letter-spacing: 1px;
    color: var(--brand-deep);
  }
  .header-rule {
    position: absolute;
    left: 0;
    right: 0;
    top: 75px;
    height: 2px;
    background: var(--brand-blue);
  }
  .contact-line {
    position: absolute;
    left: 72px;
    top: 80px;
    font-size: 13px;
    color: var(--brand-blue);
    white-space: nowrap;
  }
  .background-mark {
    position: absolute;
    left: 0;
    right: 0;
    top: 312px;
    text-align: center;
    font-weight: 700;
    font-size: 200px;
    line-height: 1;
    color: var(--mark-faint);
  }
  .footer-rules {
    position: absolute;
    left: 0;
    top: 770px;
    width: 438px;
    height: 5px;
    border-top: 2px solid var(--brand-blue);
    border-bottom: 2px solid var(--brand-blue);
  }
  .footer-brand {
    position: absolute;
    left: 446px;
    top: 765px;
    font-weight: 700;
    font-size: 12px;
    color: var(--brand-deep);
    white-space: nowrap;
  }
</style>
</head>
<body>
  <main class="letterhead">
    <header>
      <div class="brand-name">Bright Crest Lifts</div>
      <div class="header-rule"></div>
      <p class="contact-line">your name, adress, phone numbers, web adress, email etc...........................</p>
    </header>
    <div class="background-mark" aria-hidden="true">BCL</div>
    <footer>
      <div class="footer-rules"></div>
      <div class="footer-brand">Bright Crest Lifts</div>
    </footer>
  </main>
</body>
</html>
```